DM - management consultant

Business card - contemporary design

Front info
Dorian Maples

(Address not necessary)
PO Box 7386
Belmont, CA 94002

(650) 555-0143
dm@dorianmapl.es

Chirper: dmq527
Facepage: /Dorian.Maples
Linkline: /in/dorianmaples

Back or Front
www.dorianmaples.net
Facilitation & coaching, change management, strategic partnerships, business improvement

Target Market(s)

High tech businesses - mostly startups in Silicon Valley

Industry/Entity Type

Business

Font styles to use
Sans Serif

Colors

Designer to choose colors to be used in the design.

```html
<!DOCTYPE html>
<html lang="en">
<head>
<meta charset="utf-8">
<title>Dorian Maples – Business Card</title>
<link href="https://fonts.googleapis.com/css2?family=Arimo:wght@400;700&family=Lato:wght@400&display=swap" rel="stylesheet">
<style>
  :root {
    --page: #ffffff;
    --ink: #111111;
    --card-deep: #0c111d;
    --card-mid: #172033;
    --card-blue: #22335a;
    --text-light: #f2f4f8;
    --text-soft: #c9ced8;
    --rule: rgba(200, 208, 222, 0.28);
    --brand: #c8ccd4;
    --gold: #f1d8a6;
    --url-box: #05070c;
  }
  * { margin: 0; padding: 0; box-sizing: border-box; }
  html, body {
    width: 939px; height: 1200px; overflow: hidden;
    background: var(--page);
    font-family: "Arimo", Arial, sans-serif;
  }
  .sheet { position: relative; width: 939px; height: 1200px; }

  .side-label {
    position: absolute; left: 0; width: 939px; text-align: center;
    font-size: 31px; font-weight: 400; color: var(--ink); letter-spacing: 0.5px;
  }
  .side-label--front { top: 40px; }
  .side-label--back { top: 583px; }

  .card {
    position: absolute; overflow: hidden;
    box-shadow: 0 16px 18px -6px rgba(0,0,0,0.5);
  }
  .card--front { left: 84px; top: 91px; width: 722px; height: 410px; }
  .card--back { left: 89px; top: 643px; width: 722px; height: 410px; }

  .card__texture {
    position: absolute; inset: 0;
    background:
      radial-gradient(ellipse at 80% 90%, var(--card-blue) 0%, transparent 50%),
      radial-gradient(ellipse at 8% 15%, #1d2943 0%, transparent 45%),
      linear-gradient(135deg, var(--card-mid) 0%, var(--card-deep) 55%, #131a2c 100%);
  }

  .brand {
    position: absolute; left: 0; width: 100%; top: 58px;
    display: flex; align-items: center; justify-content: center; gap: 14px;
    font-size: 40px; font-weight: 400; color: var(--brand); line-height: 1;
  }
  .brand__square { width: 34px; height: 34px; background: var(--brand); flex: none; }

  .rule {
    position: absolute; height: 2px;
    background: linear-gradient(90deg, transparent, var(--text-soft), transparent);
  }
  .rule--upper { left: 200px; width: 340px; top: 148px; }
  .rule--lower { left: 200px; width: 340px; top: 208px; }
  .name {
    position: absolute; left: 0; width: 100%; top: 161px; text-align: center;
    font-size: 33px; font-weight: 400; color: var(--text-light); letter-spacing: 0.3px;
  }
  .role {
    position: absolute; left: 0; width: 100%; top: 224px; text-align: center;
    font-family: "Lato", "Gill Sans", sans-serif; font-size: 17px; color: var(--text-soft);
  }

  .contact-row, .social-row {
    position: absolute; display: flex; align-items: center;
    color: var(--text-light); font-weight: 700;
  }
  .contact-row { left: 40px; font-size: 20px; gap: 20px; }
  .contact-row--phone { top: 300px; }
  .contact-row--mail { top: 346px; }
  .contact-row svg { width: 40px; height: 34px; flex: none; }

  .social-row { left: 424px; font-size: 16px; gap: 18px; }
  .social-row--one { top: 293px; }
  .social-row--two { top: 329px; }
  .social-row--three { top: 360px; }
  .social-mark { width: 22px; height: 22px; background: var(--text-light); flex: none; }

  .line { position: absolute; height: 1px; background: var(--rule); }

  .url-box {
    position: absolute; left: 189px; top: 124px; width: 374px; height: 59px;
    background: var(--url-box);
    display: flex; align-items: center; justify-content: center;
    font-size: 26px; font-weight: 700; color: var(--gold);
  }
  .service {
    position: absolute; display: flex; align-items: center; gap: 14px;
    color: var(--text-light); font-size: 22px; font-weight: 700;
  }
  .service svg { width: 36px; height: 36px; flex: none; }
  .service--a { left: 30px; top: 265px; }
  .service--b { left: 30px; top: 311px; }
  .service--c { left: 374px; top: 265px; }
  .service--d { left: 374px; top: 311px; }
</style>
</head>
<body>
<div class="sheet">

  <h2 class="side-label side-label--front">FRONT</h2>
  <section class="card card--front">
    <div class="card__texture" role="img" aria-label="Dark navy faceted low-poly background"></div>
    <div class="brand"><span class="brand__square"></span><span>Dorian Maples</span></div>
    <div class="rule rule--upper"></div>
    <div class="name">DORIAN MAPLES</div>
    <div class="rule rule--lower"></div>
    <div class="role">Management Consultants</div>

    <div class="line" style="left:30px;top:290px;width:262px"></div>
    <div class="contact-row contact-row--phone">
      <svg viewBox="0 0 40 34" fill="none" stroke="#f2f4f8" stroke-width="2.4" stroke-linecap="round" stroke-linejoin="round">
        <path d="M8 6 l6 -2 l4 8 l-4 3 c2 4 5 7 9 9 l3 -4 l8 4 l-2 6 c-12 1 -25 -12 -24 -24 z"/>
        <path d="M24 4 a10 10 0 0 1 9 9"/>
        <path d="M23 9 a5 5 0 0 1 5 5"/>
      </svg>
      <span>(650) 555-0143</span>
    </div>
    <div class="line" style="left:30px;top:336px;width:262px"></div>
    <div class="contact-row contact-row--mail">
      <svg viewBox="0 0 40 34" fill="none" stroke="#f2f4f8" stroke-width="2.4" stroke-linejoin="round">
        <rect x="5" y="7" width="30" height="20"/>
        <path d="M5 7 l15 12 l15 -12"/>
      </svg>
      <span>dm@dorianmapl.es</span>
    </div>

    <div class="line" style="left:405px;top:282px;width:310px"></div>
    <div class="social-row social-row--one"><span class="social-mark"></span><span>Chirper: dmq527</span></div>
    <div class="line" style="left:405px;top:320px;width:310px"></div>
    <div class="social-row social-row--two"><span class="social-mark"></span><span>Linkline: /in/dorianmaples</span></div>
    <div class="line" style="left:405px;top:353px;width:310px"></div>
    <div class="social-row social-row--three"><span class="social-mark"></span><span>Facepage: /Dorian.Maples</span></div>
  </section>

  <h2 class="side-label side-label--back">BACK</h2>
  <section class="card card--back">
    <div class="card__texture" role="img" aria-label="Dark navy faceted low-poly background"></div>
    <div class="url-box">www.dorianmaples.net</div>

    <div class="service service--a">
      <svg viewBox="0 0 36 36" fill="none" stroke="#f2f4f8" stroke-width="3"><rect x="3" y="6" width="27" height="27"/><path d="M9 18 l6 7 l15 -22" stroke-width="4"/></svg>
      <span>Facilitation &amp; Coaching</span>
    </div>
    <div class="line" style="left:28px;top:306px;width:320px"></div>
    <div class="service service--b">
      <svg viewBox="0 0 36 36" fill="none" stroke="#f2f4f8" stroke-width="3"><rect x="3" y="6" width="27" height="27"/><path d="M9 18 l6 7 l15 -22" stroke-width="4"/></svg>
      <span>Change Management</span>
    </div>
    <div class="line" style="left:28px;top:352px;width:320px"></div>

    <div class="service service--c">
      <svg viewBox="0 0 36 36" fill="none" stroke="#f2f4f8" stroke-width="3"><rect x="3" y="6" width="27" height="27"/><path d="M9 18 l6 7 l15 -22" stroke-width="4"/></svg>
      <span>Strategic Partnerships</span>
    </div>
    <div class="line" style="left:372px;top:306px;width:320px"></div>
    <div class="service service--d">
      <svg viewBox="0 0 36 36" fill="none" stroke="#f2f4f8" stroke-width="3"><rect x="3" y="6" width="27" height="27"/><path d="M9 18 l6 7 l15 -22" stroke-width="4"/></svg>
      <span>Business Improvement</span>
    </div>
    <div class="line" style="left:372px;top:352px;width:320px"></div>
  </section>

</div>
</body>
</html>
```